A New Website - Harrowgate Meridian Trade Council

Website Brief for Harrowgate and Meridian Trade Council
Overview

The chamber needs to revamp the current website that is not working.
www.harrowgatemeridiancouncil.example
We are looking to revamp the website and create a new professional, user-friendly, and dynamic website to showcase the chamber's services while allowing minimal day-to-day interference for the in house team.

The Chamber and members use the website for :
1. Presenting the chamber , members, activities and services to the business community.
2. The User will be able to
1. See our activities, events and register interest
2. Access membership information, benefits and register using an external link ( Pellmore Reach )
3. Access News and reports that our team posts ( either in the website or using an external source)
4. Business will be able to access our members Directory ( in the website or outside throgh links)
5. Include a Quibbly Chat for easy access to our team with an initial set of automated responses.

The rest of the pages will offer general information about the chamber, our structure and our services .

Target Market(s)

Corporates , Governments & Business Executives

Industry/Entity Type

Chamber of Commerce

Coding

Coded - Design and coding required

Number of Pages Required

5+ page

Font styles to use
Sans Serif
Other font styles liked:
• we are suing georgia in house for all publications

Colors
0054AA
0677BA
7BADD7
CADEEF
E8F1F8
FFF300
FFF600
FEFA6F
FFFEC7
FFFEE8
EB3D1F
EC4F4E
F09395
F8D3D4
FCEDEE

Requirements
Must have
• A clean Design, corporate , with high quality images mainly hours and a few generic ones.
Nice to have
• Responsive, user friendly quick
Should not have
• should not be busy , or chidish..

```html
<!DOCTYPE html>
<html lang="en">
<head>
<meta charset="utf-8">
<title>Harrowgate Meridian Trade Council</title>
<link rel="stylesheet" href="https://fonts.googleapis.com/css2?family=Poppins:ital,wght@0,400;0,500;0,600;0,700;1,400&display=swap">
<style>
:root{
  --navy:#173f8f;
  --navy-deep:#1d3f93;
  --heading:#1a3d8f;
  --red:#e2231f;
  --yellow:#fff300;
  --pale-blue:#e3edf6;
  --grey-band:#efefef;
  --text:#333;
  --muted:#8a8a8a;
  --white:#fff;
}
*{margin:0;padding:0;box-sizing:border-box}
html,body{width:1200px;height:4926px;overflow:hidden}
body{font-family:'Poppins',sans-serif;color:var(--text);background:var(--white);position:relative}
.abs{position:absolute}
.btn{position:absolute;display:flex;align-items:center;justify-content:center;font-weight:600;font-size:13px;color:var(--white);background:var(--red);white-space:nowrap}
.btn.outline{background:transparent;border:2px solid var(--white)}
.btn.outline-yellow{background:transparent;border:2px solid var(--yellow)}
.btn.outline-red{background:var(--white);border:1.5px solid var(--red);color:var(--red)}

/* top bar */
.topbar{position:absolute;left:0;top:0;width:1200px;height:50px;background:var(--navy);color:var(--white);font-size:13px;font-weight:600}
.topbar .hours{position:absolute;left:73px;top:15px;display:flex;align-items:center;gap:8px}
.topbar .phone{position:absolute;left:334px;top:15px;display:flex;align-items:center;gap:7px}
.social{position:absolute;right:74px;top:13px;display:flex;gap:18px}
.social span{width:22px;height:22px;border-radius:50%;border:2px solid var(--white)}

/* nav */
.brand{position:absolute;left:76px;top:66px;display:flex;align-items:center;gap:7px}
.brand .dot{width:18px;height:18px;border-radius:50%;background:var(--navy)}
.brand .name{font-size:10.5px;font-weight:600;color:var(--navy);line-height:13px;width:82px}
.nav{position:absolute;right:74px;top:95px;display:flex;gap:24px;font-size:13.5px;font-weight:500;color:#222}
.nav .active{color:var(--red);font-weight:600}

/* hero */
.hero{position:absolute;left:0;top:160px;width:1200px;height:566px;background:linear-gradient(100deg,#3a3f4a 0%,#6b5a4c 25%,#34383f 48%,#1c2028 70%,#0f1218 100%)}
.hero h1{position:absolute;left:630px;top:140px;font-size:70px;font-weight:700;color:var(--white);line-height:1}
.hero p{position:absolute;left:631px;top:240px;width:505px;font-size:18.5px;line-height:30px;color:var(--white)}
.dots{position:absolute;left:74px;top:503px;display:flex;gap:11px}
.dots span{width:14px;height:14px;border-radius:50%;background:var(--white)}
.dots span.on{background:var(--yellow)}

/* about */
.section-title{font-size:33px;font-weight:700;color:var(--heading);line-height:1.2}
.section-title .light{font-weight:400}
.about-text{position:absolute;left:75px;top:864px;width:515px;font-size:13.3px;line-height:24.2px;color:#333}
.photo{position:absolute}

/* members */
.members-title{position:absolute;left:0;width:1200px;top:1298px;text-align:center;font-size:23px;font-weight:700;color:var(--red)}
.rule{position:absolute;top:1315px;height:1px;background:#bbb}
.member{position:absolute;top:1372px;height:68px;display:flex;align-items:center;justify-content:center;font-size:34px;font-weight:500;color:#8a8a8a;white-space:nowrap}
.member.focus{border:2px solid var(--heading);color:#6d6d6d}
.arrow{position:absolute}

/* find us */
.findus{position:absolute;left:75px;top:1506px;width:1051px;height:212px;background:var(--pale-blue)}
.findus h2{position:absolute;left:83px;top:42px;font-size:32px;font-weight:700;color:var(--heading);line-height:1.2}
.findus h3{position:absolute;left:83px;top:82px;font-size:28px;font-weight:600;color:var(--red);line-height:1.2}
.findus p{position:absolute;left:84px;top:124px;font-size:12.5px;line-height:23px;color:#333}

/* why join */
.why{position:absolute;left:0;top:1785px;width:1200px;height:502px;background:linear-gradient(115deg,#3a3a3e 0%,#272a31 40%,#1e222a 70%,#2d2b30 100%)}
.why h2{position:absolute;left:0;width:1200px;top:50px;text-align:center;font-size:32px;font-weight:600;color:var(--white)}
.stat{position:absolute;font-size:72px;font-weight:700;color:var(--yellow);line-height:1}
.stat-label{position:absolute;font-size:16px;line-height:25px;color:var(--white)}
.why .note{position:absolute;left:0;width:1200px;top:350px;text-align:center;font-size:16px;color:var(--yellow)}

/* panels */
.panel{position:absolute;background:var(--pale-blue)}
.panel h2{position:absolute;left:22px;top:32px;font-size:33px;font-weight:700;color:var(--heading);line-height:39px}
.panel p{position:absolute;left:22px;width:405px;font-size:12.5px;line-height:23px;color:#333}

/* testimonials */
.testi-title{position:absolute;left:0;width:1200px;top:2960px;text-align:center;font-size:33px;line-height:40px;color:var(--heading)}
.card{position:absolute;top:3075px;height:262px;background:var(--white);border:1px solid #d6d6d6}
.card.raised{box-shadow:0 4px 16px rgba(0,0,0,.18);border-color:#e2e2e2}
.card .q{position:absolute;left:14px;top:-2px;font-size:64px;color:#cfcfcf;line-height:1;font-family:Georgia,serif}
.card .q.close{left:auto;right:18px;top:auto;bottom:10px}
.card p{position:absolute;left:18px;top:30px;right:18px;font-size:12.5px;line-height:23px;font-style:italic;color:#444}
.card .avatar{position:absolute;width:60px;height:60px;border-radius:50%;background:linear-gradient(160deg,#c9a98c,#6b5242)}
.card .who{position:absolute;right:12px;font-size:12px;line-height:19px;color:#333}
.card .who b{display:block;color:var(--red);font-weight:600;font-size:13.5px}

/* events */
.events{position:absolute;left:0;top:3407px;width:1200px;height:507px;background:var(--grey-band)}
.events p{position:absolute;left:75px;top:165px;width:485px;font-size:13.3px;line-height:24.2px;color:#333}

/* footer */
.footer{position:absolute;left:0;top:4544px;width:1200px;height:382px;background:var(--navy-deep);color:var(--white)}
.footer .mark{position:absolute;left:147px;top:86px;width:70px;height:70px;border-radius:50%;background:var(--white)}
.footer .mark-name{position:absolute;left:95px;top:166px;width:180px;text-align:center;font-size:13px;font-weight:600;line-height:18px}
.footer .copy{position:absolute;left:70px;top:252px;width:230px;text-align:center;font-size:13px;line-height:20px}
.fcol{position:absolute;top:70px}
.fcol h4{font-size:18px;font-weight:600;line-height:24px;margin-bottom:8px}
.fcol li{list-style:none;font-size:12.5px;line-height:29px}
</style>
</head>
<body>

<header class="topbar">
  <div class="hours">
    <svg width="14" height="14" viewBox="0 0 14 14"><circle cx="7" cy="7" r="6" fill="none" stroke="#fff" stroke-width="1.6"/><path d="M7 3.5V7l2.3 1.6" fill="none" stroke="#fff" stroke-width="1.6" stroke-linecap="round"/></svg>
    Monday - Friday 09:30-17:00.
  </div>
  <div class="phone">
    <svg width="13" height="14" viewBox="0 0 13 14"><path d="M3 1l2 3-1.3 1.4c.8 1.8 2.2 3.3 4 4.2L9.2 8l3 2-1 2.6C6.2 13 1 7.8 1 2.2z" fill="none" stroke="#fff" stroke-width="1.4" stroke-linejoin="round"/></svg>
    (+44) 207 555 0148
  </div>
  <div class="social" aria-label="Social channels"><span></span><span></span><span></span><span></span><span></span></div>
</header>

<div class="brand">
  <span class="dot"></span>
  <span class="name">Harrowgate Meridian Trade Council</span>
</div>
<nav class="nav">
  <span class="active">Home</span><span>About Us</span><span>Resources</span><span>Resources</span><span>News</span><span>Community News</span><span>Media Centre</span><span>Legal</span><span>Work with Us</span><span>Contact Us</span>
</nav>

<section class="hero" role="img" aria-label="Delegates seated at a panel table during a trade conference">
  <h1>Engage</h1>
  <p>Joining the HMTC gives you access to a wide range of business services, from networking events to bespoke advice.</p>
  <div class="btn" style="left:631px;top:356px;width:150px;height:42px">Get Started</div>
  <div class="btn outline" style="left:793px;top:356px;width:151px;height:42px">See Benefits</div>
  <div class="btn outline-yellow" style="left:956px;top:356px;width:149px;height:42px">Get Involved</div>
  <div class="dots"><span class="on"></span><span></span><span></span><span></span></div>
</section>

<h2 class="section-title abs" style="left:75px;top:804px">About Us</h2>
<div class="btn outline-red" style="left:950px;top:802px;width:176px;height:45px">Timeline</div>
<p class="about-text">The Harrowgate Meridian Trade Council stands as a leading international business organisation, uniting members committed to responsible economic and social development, open markets and the principles of the rule of law and democracy. Its membership comprises prominent global companies across a diverse range of sectors, including banking and finance, consulting, consumer goods, energy and mining, manufacturing, media, tourism, technology and infrastructure.<br>Through this broad spectrum of industries, the Council fosters a collaborative environment where leaders work towards sustainable growth and mutual prosperity in the UK, Colombia, and Latin America.</p>
<div class="btn" style="left:75px;top:1133px;width:355px;height:44px">Meet Our Board of Directors &amp; Team</div>
<div class="btn" style="left:75px;top:1190px;width:355px;height:44px">Jobs and Work Experience Opportunities</div>
<div class="photo" style="left:613px;top:869px;width:513px;height:367px;background:linear-gradient(160deg,#c9b79a 0%,#8a7c68 40%,#3b3836 75%,#58423c 100%)" role="img" aria-label="Group of council members standing together at a reception"></div>

<div class="rule" style="left:75px;width:357px"></div>
<div class="rule" style="left:767px;width:359px"></div>
<h2 class="members-title">Meet Our Members</h2>
<svg class="arrow" style="left:46px;top:1395px" width="14" height="24" viewBox="0 0 14 24"><path d="M11 3L3 12l8 9" fill="none" stroke="#555" stroke-width="2.2"/></svg>
<div class="member" style="left:76px;width:150px">Quellary</div>
<div class="member" style="left:288px;width:192px;font-size:29px">Brantwell Action</div>
<div class="member focus" style="left:518px;width:212px;font-size:31px">Paymora</div>
<div class="member" style="left:772px;width:354px;font-size:32px;font-weight:400">Vellard &amp; Vellard</div>
<svg class="arrow" style="left:1140px;top:1395px" width="14" height="24" viewBox="0 0 14 24"><path d="M3 3l8 9-8 9" fill="none" stroke="#555" stroke-width="2.2"/></svg>

<section class="findus">
  <h2>How to Find Us and Opening Times</h2>
  <h3>(By appointment only)</h3>
  <p>Open Tuesdays at the HMTC<br>Join us for a cup of coffee and get to know the Council, the business lounge and its facilities.</p>
  <div class="btn" style="left:794px;top:84px;width:174px;height:47px">Contact us</div>
</section>

<section class="why" role="img" aria-label="Busy exhibition hall with visitors at trade stands, darkened">
  <h2>Why <span style="font-weight:400">Join Us ?</span></h2>
  <div class="stat" style="left:230px;top:133px">20</div>
  <div class="stat-label" style="left:338px;top:140px">Years of trade &amp; Investment<br>support experience</div>
  <div class="stat" style="left:666px;top:133px">+17k</div>
  <div class="stat-label" style="left:846px;top:137px">High profile business<br>and government<br>contacts</div>
  <div class="stat" style="left:180px;top:245px">500</div>
  <div class="stat-label" style="left:338px;top:253px">High Profile<br>Events</div>
  <div class="stat" style="left:738px;top:245px">25</div>
  <div class="stat-label" style="left:846px;top:253px">Missions and Market<br>visits organised</div>
  <div class="note">Plus access to a&nbsp; High Profile Location right at the Centre of London</div>
  <div class="btn" style="left:512px;top:403px;width:176px;height:44px">See Benefits</div>
</section>

<div class="photo" style="left:434px;top:2358px;width:607px;height:336px;background:linear-gradient(120deg,#6b6e76 0%,#b9b3aa 40%,#e6e6ea 70%,#d3d5dc 100%)" role="img" aria-label="Speaker in front of a sponsor backdrop"></div>
<div class="photo" style="left:495px;top:2690px;width:705px;height:222px;background:linear-gradient(135deg,#0f5a78 0%,#1e7d96 50%,#0e4d6b 100%)" role="img" aria-label="Aerial view of a container ship at sea"></div>
<section class="panel" style="left:75px;top:2412px;width:449px;height:435px">
  <h2>Engage through<br><span style="font-weight:400">Membership</span></h2>
  <p style="top:122px">Join a distinguished group of individuals and engage in private discussions with senior government officials, business leaders, policymakers, and cultural figures. Emerald Members of the Council are invited to participate in exclusive events and join working groups. It also provides unlimited access to Council business services and to business lounges around the world.</p>
  <div class="btn" style="left:22px;top:298px;width:337px;height:44px">Access Benefits</div>
  <div class="btn" style="left:22px;top:351px;width:337px;height:46px">Get to know our business lounge</div>
</section>

<h2 class="testi-title"><b>What our members and</b><br>clients say about us</h2>
<svg class="arrow" style="left:44px;top:3194px" width="14" height="24" viewBox="0 0 14 24"><path d="M11 3L3 12l8 9" fill="none" stroke="#555" stroke-width="2.2"/></svg>
<svg class="arrow" style="left:1142px;top:3194px" width="14" height="24" viewBox="0 0 14 24"><path d="M3 3l8 9-8 9" fill="none" stroke="#555" stroke-width="2.2"/></svg>

<article class="card" style="left:75px;width:328px">
  <span class="q">&ldquo;</span>
  <p>The Meet the Buyer Latin America event organised by the Harrowgate Meridian Council is by far the best on-line event I have attended since I have been Export Manager at Orchardly Cider (close to 5 years)</p>
  <div class="avatar" style="left:17px;top:180px" role="img" aria-label="Portrait of the reviewer"></div>
  <div class="who" style="left:90px;top:190px"><b>Ravi Tolland, Orchardly Cider,</b>Meet The Buyer Programme</div>
</article>
<article class="card raised" style="left:438px;width:326px">
  <span class="q">&ldquo;</span>
  <p>The conference was not only intellectually stimulating but also impeccably organised, which made the experience all the more enjoyable...&rdquo;</p>
  <div class="avatar" style="left:24px;top:180px" role="img" aria-label="Portrait of the reviewer"></div>
  <div class="who" style="left:91px;top:183px;right:60px"><b>Marisol Quentero</b>GFI, Trade and Investment Conference</div>
  <span class="q close">&rdquo;</span>
</article>
<article class="card" style="left:797px;width:329px">
  <span class="q">&ldquo;</span>
  <p>We want to congratulate the HMTC for creating this initiative (the Responsible Business Awards), which is of great value for companies such as Calloway Mining Ltd, that have developed responsible business practices along their social...&rdquo;</p>
  <div class="avatar" style="left:18px;top:182px" role="img" aria-label="Portrait of the reviewer"></div>
  <div class="who" style="left:92px;top:180px"><b>DR. Alan Brereton</b>Former Minister of State at the Foreign and Commonwealth Office, HMTC services</div>
</article>

<section class="events">
  <h2 class="section-title abs" style="left:75px;top:104px">Attend <span class="light">Our Events</span></h2>
  <p>Discover our comprehensive events programme. Networking is at the heart of what we do. All of our upcoming on-demand events, as well as our partner events, bring together leading figures from politics and business together with experts from our member companies to discuss and propose solutions to prevailing economic, political and trade issues that enhance the relationship between the UK, Colombia and Latin America.</p>
  <div class="btn" style="left:75px;top:350px;width:290px;height:46px">Access Our Events Programme</div>
  <div class="photo" style="left:615px;top:58px;width:230px;height:176px;background:linear-gradient(140deg,#b7a793,#5a4d44 60%,#2c2a2c)" role="img" aria-label="Guests in conversation at a reception"></div>
  <div class="photo" style="left:877px;top:58px;width:249px;height:176px;background:linear-gradient(140deg,#8f8577,#c5c1b8 50%,#3d3b3d)" role="img" aria-label="Delegates talking at an event"></div>
  <div class="photo" style="left:615px;top:249px;width:511px;height:201px;background:linear-gradient(120deg,#a79c8c,#6d655c 45%,#2a2c32 80%)" role="img" aria-label="Attendees mingling in a formal hall"></div>
</section>

<div class="photo" style="left:434px;top:3990px;width:766px;height:472px;background:linear-gradient(120deg,#b78c6a 0%,#2a2522 40%,#3a3536 60%,#dfe3ea 85%,#c8cdd6 100%)" role="img" aria-label="Printed reports and booklets laid on a table"></div>
<section class="panel" style="left:75px;top:4036px;width:449px;height:378px">
  <h2 style="top:45px">News &amp; <span style="font-weight:400">Analysis</span></h2>
  <p style="top:103px;width:392px">Our research services are tailored to find the right partner, channel or project and fast track with confidence your expansion plans in Colombia, Latin America or the United Kingdom.</p>
  <div class="btn" style="left:22px;top:222px;width:337px;height:46px">View Insights &amp; Resources</div>
  <div class="btn" style="left:22px;top:279px;width:337px;height:46px">Stay Up to Date with Community News</div>
</section>

<footer class="footer">
  <div class="mark"></div>
  <div class="mark-name">Harrowgate Meridian<br>Trade Council</div>
  <div class="copy">Copyright 2025 &copy;<br>Harrowgate and Meridian Trade Council<br>All right reserved.</div>
  <div class="fcol" style="left:352px">
    <h4>Popular Services</h4>
    <ul><li>Membership Benefits</li><li>Membership Directory</li><li>Our Board</li><li>Events</li><li>Business Visits &amp; Market Support</li><li>Campaigns</li><li>Brand Opportunities</li></ul>
  </div>
  <div class="fcol" style="left:636px">
    <h4>Connect with<br>HMTC</h4>
    <ul><li>Chirpline</li><li>Lenswell</li><li>Circlebook</li><li>Streamly</li><li>Linkwork</li></ul>
  </div>
  <div class="fcol" style="left:860px">
    <h4>Contact Us</h4>
    <ul>
      <li style="line-height:22px">Calder House,</li>
      <li style="line-height:22px">12 Fenwright Street London,</li>
      <li style="line-height:22px">W1X 4QP, UK</li>
      <li>+44 (0) 207 555 0148</li>
      <li>info@harrowgatemeridiancouncil.example</li>
    </ul>
  </div>
</footer>

</body>
</html>
```